Fenwry T's Menu boxes

HI

This project if for the design of some illuminated menu boxes for inside a shop.

We sell Ice Cream, Milk shakes, Smoothies and some cakes.

The shop is mainly pink in colour, i have had some posters done for the windows and would like the menus to maintain the feel of the posters. i have 8 menu boards but will probably onlu use 4.

i will attach a few of the posters so you can see the feel im looking for and the menu should have:
a section for ice creams
a section for milk shakes
a section for smoothies
a section for coffees and teas
and a section for juices
and a section for desserts.

Regards
Updates

Hi

I have now attached the logos source file

Many thanks

Reason: Hi for some reason only one designer has responded therefore i am extending the deadline thanks

Hi All

I have now increased the budget on the project

Many Thanks

Industry/Entity Type

Shop

```html
<!DOCTYPE html>
<html lang="en">
<head>
<meta charset="utf-8">
<title>Fenwry T's Menu</title>
<link href="https://fonts.googleapis.com/css2?family=Montserrat:wght@600;700;800&display=swap" rel="stylesheet">
<style>
  :root {
    --paper: #fbfbfb;
    --ink: #1c1c1c;
    --heading: #f07a2a;
    --brand: #a3228f;
    --dollar: #e0218a;
    --price: #3a3a3a;
    --choc: #6b3b1c;
    --cream: #f4f1ec;
    --cone: #f2a444;
    --glass: #bcd8ef;
  }
  * { margin: 0; padding: 0; box-sizing: border-box; }
  html, body { width: 848px; height: 1200px; overflow: hidden; background: var(--paper); }
  .menu {
    position: relative;
    width: 848px;
    height: 1200px;
    overflow: hidden;
    background: var(--paper);
    font-family: "Montserrat", Arial, sans-serif;
    color: var(--ink);
  }
  .brand-name {
    position: absolute;
    left: 28px;
    top: 108px;
    font-family: "Montserrat", Arial, sans-serif;
    font-weight: 800;
    font-size: 64px;
    line-height: 1;
    color: var(--brand);
    letter-spacing: -1px;
  }
  .art {
    position: absolute;
    display: block;
  }
  .art-sundae {
    left: 548px; top: 48px; width: 240px; height: 212px;
    border-radius: 40% 40% 22% 22%;
    background: linear-gradient(180deg, var(--cream) 0%, var(--cream) 42%, var(--choc) 60%, #4a2812 100%);
  }
  .art-banana-split {
    left: 540px; top: 496px; width: 300px; height: 204px;
    border-radius: 48% 48% 30% 30%;
    background: linear-gradient(180deg, #e8404c 0%, #f4d2d6 35%, #b9c94a 55%, var(--cream) 72%, var(--cone) 100%);
  }
  .art-shake-coffee {
    left: 10px; top: 804px; width: 300px; height: 382px;
    border-radius: 46% 40% 14% 14%;
    background: linear-gradient(160deg, var(--cream) 0%, var(--glass) 38%, #c58b5c 62%, var(--cone) 100%);
  }
  .section {
    position: absolute;
  }
  .section-title {
    font-weight: 700;
    font-size: 19px;
    line-height: 20px;
    color: var(--heading);
  }
  .items {
    list-style: none;
    margin-top: -1.5px;
  }
  .item {
    display: flex;
    font-weight: 700;
    font-size: 13px;
    line-height: 33px;
    height: 33px;
  }
  .item-name { width: 151px; }
  .item-price { color: var(--price); font-weight: 600; }
  .item-price .currency { color: var(--dollar); }
  .ice-creams { left: 44px; top: 271px; }
  .milk-shakes { left: 44px; top: 549px; }
  .smoothies { left: 326px; top: 271px; }
  .coffees-teas { left: 326px; top: 682px; }
  .juices { left: 605px; top: 271px; }
  .desserts { left: 605px; top: 749px; }
</style>
</head>
<body>
<main class="menu">
  <h1 class="brand-name">Fenwry T's</h1>

  <div class="art art-sundae" role="img" aria-label="Illustration of a chocolate brownie sundae with ice cream, sprinkles and a wafer"></div>
  <div class="art art-banana-split" role="img" aria-label="Illustration of a banana split with scoops of ice cream, whipped cream and a cherry"></div>
  <div class="art art-shake-coffee" role="img" aria-label="Illustration of a milkshake with a cherry, a cup of coffee, a croissant and a muffin"></div>

  <section class="section ice-creams">
    <h2 class="section-title">Ice Creams</h2>
    <ul class="items">
      <li class="item"><span class="item-name">Ice Cream</span><span class="item-price"><span class="currency">$</span>00</span></li>
      <li class="item"><span class="item-name">Ice Cream</span><span class="item-price"><span class="currency">$</span>00</span></li>
      <li class="item"><span class="item-name">Ice Cream</span><span class="item-price"><span class="currency">$</span>00</span></li>
      <li class="item"><span class="item-name">Ice Cream</span><span class="item-price"><span class="currency">$</span>00</span></li>
      <li class="item"><span class="item-name">Ice Cream</span><span class="item-price"><span class="currency">$</span>00</span></li>
      <li class="item"><span class="item-name">Ice Cream</span><span class="item-price"><span class="currency">$</span>00</span></li>
      <li class="item"><span class="item-name">Ice Cream</span><span class="item-price"><span class="currency">$</span>00</span></li>
    </ul>
  </section>

  <section class="section milk-shakes">
    <h2 class="section-title">Milk Shakes</h2>
    <ul class="items">
      <li class="item"><span class="item-name">Milk Shakes</span><span class="item-price"><span class="currency">$</span>00</span></li>
      <li class="item"><span class="item-name">Milk Shakes</span><span class="item-price"><span class="currency">$</span>00</span></li>
      <li class="item"><span class="item-name">Milk Shakes</span><span class="item-price"><span class="currency">$</span>00</span></li>
      <li class="item"><span class="item-name">Milk Shakes</span><span class="item-price"><span class="currency">$</span>00</span></li>
      <li class="item"><span class="item-name">Milk Shakes</span><span class="item-price"><span class="currency">$</span>00</span></li>
      <li class="item"><span class="item-name">Milk Shakes</span><span class="item-price"><span class="currency">$</span>00</span></li>
      <li class="item"><span class="item-name">Milk Shakes</span><span class="item-price"><span class="currency">$</span>00</span></li>
    </ul>
  </section>

  <section class="section smoothies">
    <h2 class="section-title">Smoothies</h2>
    <ul class="items">
      <li class="item"><span class="item-name">Smoothies</span><span class="item-price"><span class="currency">$</span>00</span></li>
      <li class="item"><span class="item-name">Smoothies</span><span class="item-price"><span class="currency">$</span>00</span></li>
      <li class="item"><span class="item-name">Smoothies</span><span class="item-price"><span class="currency">$</span>00</span></li>
      <li class="item"><span class="item-name">Smoothies</span><span class="item-price"><span class="currency">$</span>00</span></li>
      <li class="item"><span class="item-name">Smoothies</span><span class="item-price"><span class="currency">$</span>00</span></li>
      <li class="item"><span class="item-name">Smoothies</span><span class="item-price"><span class="currency">$</span>00</span></li>
      <li class="item"><span class="item-name">Smoothies</span><span class="item-price"><span class="currency">$</span>00</span></li>
      <li class="item"><span class="item-name">Smoothies</span><span class="item-price"><span class="currency">$</span>00</span></li>
      <li class="item"><span class="item-name">Smoothies</span><span class="item-price"><span class="currency">$</span>00</span></li>
      <li class="item"><span class="item-name">Smoothies</span><span class="item-price"><span class="currency">$</span>00</span></li>
      <li class="item"><span class="item-name">Smoothies</span><span class="item-price"><span class="currency">$</span>00</span></li>
    </ul>
  </section>

  <section class="section coffees-teas">
    <h2 class="section-title">Coffees &amp; Teas</h2>
    <ul class="items">
      <li class="item"><span class="item-name">Coffees &amp; Teas</span><span class="item-price"><span class="currency">$</span>00</span></li>
      <li class="item"><span class="item-name">Coffees &amp; Teas</span><span class="item-price"><span class="currency">$</span>00</span></li>
      <li class="item"><span class="item-name">Coffees &amp; Teas</span><span class="item-price"><span class="currency">$</span>00</span></li>
      <li class="item"><span class="item-name">Coffees &amp; Teas</span><span class="item-price"><span class="currency">$</span>00</span></li>
      <li class="item"><span class="item-name">Coffees &amp; Teas</span><span class="item-price"><span class="currency">$</span>00</span></li>
      <li class="item"><span class="item-name">Coffees &amp; Teas</span><span class="item-price"><span class="currency">$</span>00</span></li>
      <li class="item"><span class="item-name">Coffees &amp; Teas</span><span class="item-price"><span class="currency">$</span>00</span></li>
      <li class="item"><span class="item-name">Coffees &amp; Teas</span><span class="item-price"><span class="currency">$</span>00</span></li>
    </ul>
  </section>

  <section class="section juices">
    <h2 class="section-title">Juices</h2>
    <ul class="items">
      <li class="item"><span class="item-name">Juice</span><span class="item-price"><span class="currency">$</span>00</span></li>
      <li class="item"><span class="item-name">Juice</span><span class="item-price"><span class="currency">$</span>00</span></li>
      <li class="item"><span class="item-name">Juice</span><span class="item-price"><span class="currency">$</span>00</span></li>
      <li class="item"><span class="item-name">Juice</span><span class="item-price"><span class="currency">$</span>00</span></li>
      <li class="item"><span class="item-name">Juice</span><span class="item-price"><span class="currency">$</span>00</span></li>
      <li class="item"><span class="item-name">Juice</span><span class="item-price"><span class="currency">$</span>00</span></li>
    </ul>
  </section>

  <section class="section desserts">
    <h2 class="section-title">Desserts</h2>
    <ul class="items">
      <li class="item"><span class="item-name">Dessert</span><span class="item-price"><span class="currency">$</span>00</span></li>
      <li class="item"><span class="item-name">Dessert</span><span class="item-price"><span class="currency">$</span>00</span></li>
      <li class="item"><span class="item-name">Dessert</span><span class="item-price"><span class="currency">$</span>00</span></li>
      <li class="item"><span class="item-name">Dessert</span><span class="item-price"><span class="currency">$</span>00</span></li>
      <li class="item"><span class="item-name">Dessert</span><span class="item-price"><span class="currency">$</span>00</span></li>
      <li class="item"><span class="item-name">Dessert</span><span class="item-price"><span class="currency">$</span>00</span></li>
      <li class="item"><span class="item-name">Dessert</span><span class="item-price"><span class="currency">$</span>00</span></li>
      <li class="item"><span class="item-name">Dessert</span><span class="item-price"><span class="currency">$</span>00</span></li>
      <li class="item"><span class="item-name">Dessert</span><span class="item-price"><span class="currency">$</span>00</span></li>
      <li class="item"><span class="item-name">Dessert</span><span class="item-price"><span class="currency">$</span>00</span></li>
      <li class="item"><span class="item-name">Dessert</span><span class="item-price"><span class="currency">$</span>00</span></li>
    </ul>
  </section>
</main>
</body>
</html>
```